Freelance yoga teacher looking for professional postcard design

I need a postcard that shows my class times & venues. I also would like it to show that I offer private one to one sessions for those not ready for group practice, or who require personal attention. It needs to show my contact details - mob: 07346218850, email & website addresses. I also want the opportunity to add other services in future, such as my website and yoga massage.

UPDATE 18 JULY

FRONT OF POSTCARD
I would like the front side of the postcard to not look too busy or 'wordy'. If using bullet points, be creative, so no ticks. Please use my full name Maren T Holloway NCM Dip.

REVERSE SIDE
The reverse side I think should have the NCM logo, together with words describing classes, 'classes are designed...' please omit the sentences starting 'by running courses...'

'Postage required' or lines for an address are not required.

Make the 'where I teach' venues/times look personable, so no harsh gridlines please.

Target Market(s)

Most of my students are 30+ professionals with disposable income or early retirees.

Industry/Entity Type

Teacher

Requirements
Must have
• It must show my National Circle of Movement Teacher Logo which I can supply.
Maren T Holloway is a National Circle of Movement trained teacher.
Classes are small and friendly, designed to create ease in the body, reduce stress and promote relaxation. Maren is passionate about sharing yoga, respecting each individual and modifying to suit their needs, leading to improved function, mobility and stability.

Keep any images simple, such as rolled up yoga mats. I am commissioning a personal mandala which I will use as a logo, but this will not be ready until mid to late August.

Please see attached 'attempt' at a postcard giving details of classes/venues, contact info.
Nice to have
• Somewhere on the postcard the words: 'Yoga. Centre the body & mind. Stretch the possibilities.'
Should not have
• Images of people doing yoga or silhouettes of yoga postures.

```html
<!DOCTYPE html>
<html lang="en">
<head>
<meta charset="utf-8">
<title>Maren T Holloway – Yoga Postcard</title>
<link rel="stylesheet" href="https://fonts.googleapis.com/css2?family=Open+Sans:wght@400;700&family=PT+Serif:wght@400;700&display=swap">
<style>
  :root {
    --brand-blue: #1b5a8e;
    --title-yellow: #f3ea1c;
    --ink: #1f1f1f;
    --paper: #ffffff;
    --mark-tint: #e9eff5;
  }
  * { box-sizing: border-box; margin: 0; padding: 0; }
  html, body { width: 1200px; height: 462px; overflow: hidden; background: var(--paper); }
  .postcard { position: relative; width: 1200px; height: 462px; display: flex; justify-content: space-between; }
  .side { position: relative; width: 598px; height: 462px; border: 2px solid var(--brand-blue); background: var(--paper); overflow: hidden; }

  /* Front */
  .name-band { position: absolute; left: 0; right: 0; top: 30px; height: 60px; background: var(--brand-blue);
    display: flex; align-items: center; justify-content: center; }
  .name-band h1 { font-family: "Open Sans", sans-serif; font-weight: 700; font-size: 33px; color: var(--title-yellow); letter-spacing: 0.5px; }
  .faint-mark { position: absolute; left: 200px; top: 100px; width: 200px; height: 200px; border-radius: 50%; background: var(--mark-tint); opacity: 0.45; }
  .details { position: absolute; left: 66px; top: 140px; list-style: none; font-family: "Open Sans", sans-serif; font-size: 17px; color: var(--ink); }
  .details li { display: flex; align-items: flex-end; height: 44.5px; }
  .details .dot { width: 14px; height: 14px; border-radius: 50%; background: var(--ink); margin: 0 22px 5px 0; flex: none; }
  .details .label { white-space: nowrap; }
  .details .fill-line { display: inline-block; border-bottom: 1px solid var(--ink); height: 1px; margin: 0 0 5px 4px; }
  .offer-band { position: absolute; left: 0; right: 0; bottom: 0; height: 60px; background: var(--brand-blue);
    display: flex; align-items: center; justify-content: center; text-align: center;
    font-family: "Open Sans", sans-serif; font-weight: 700; font-size: 15px; line-height: 21px; color: var(--paper); }

  /* Reverse */
  .accent-band { position: absolute; left: 0; right: 0; top: 76px; height: 46px; background: var(--brand-blue); }
  .teacher-mark { position: absolute; left: 225px; top: 36px; width: 144px; height: 228px; background: var(--paper);
    display: flex; flex-direction: column; align-items: center; justify-content: flex-end; padding-bottom: 8px; }
  .teacher-mark .mark-circle { width: 110px; height: 110px; border-radius: 50%; background: var(--brand-blue); margin-bottom: 18px; }
  .teacher-mark .mark-name { font-family: "PT Serif", serif; font-weight: 400; font-size: 11px; line-height: 14px; color: var(--brand-blue); text-align: center; letter-spacing: 0.5px; }
  .class-heading { position: absolute; left: 0; right: 0; top: 304px; text-align: center;
    font-family: "PT Serif", serif; font-weight: 700; font-size: 24px; color: var(--brand-blue); }
  .class-description { position: absolute; left: 24px; right: 20px; top: 344px;
    font-family: "PT Serif", serif; font-size: 16px; line-height: 23px; color: var(--ink); }
</style>
</head>
<body>
<main class="postcard">
  <section class="side side-front">
    <div class="name-band"><h1>MAREN T HOLLOWAY</h1></div>
    <div class="faint-mark" aria-hidden="true"></div>
    <ul class="details">
      <li><span class="dot"></span><span class="label">Class Times :</span><span class="fill-line" style="width:272px"></span></li>
      <li><span class="dot"></span><span class="label">Venues Time :</span><span class="fill-line" style="width:262px"></span></li>
      <li><span class="dot"></span><span class="label">Mobile No. : 07346218850</span></li>
      <li><span class="dot"></span><span class="label">Email Address :</span><span class="fill-line" style="width:254px"></span></li>
      <li><span class="dot"></span><span class="label">Website Address :</span><span class="fill-line" style="width:232px"></span></li>
    </ul>
    <div class="offer-band"><p>I offer private one to one sessions for those not ready for group practice,<br>or who require personal attention.</p></div>
  </section>

  <section class="side side-reverse">
    <div class="accent-band"></div>
    <div class="teacher-mark">
      <span class="mark-circle" aria-hidden="true"></span>
      <p class="mark-name">NATIONAL CIRCLE OF MOVEMENT<br>TEACHER</p>
    </div>
    <h2 class="class-heading">Yoga with Maren T Holloway</h2>
    <p class="class-description">Classes are small and friendly, designed to create ease in the body, reduce stress and promote relaxation. Maren is passionate about sharing yoga, respecting each individual and modifying to suit their needs, leading to improved function, mobility and stability.</p>
  </section>
</main>
</body>
</html>
```